M&A Advisory firm needs elegant and powerful letterhead

We need a powerful but elegant letterhead to engage with the international financial industry.

Target Market(s)

New York and International Financial Industry

Industry/Entity Type

Finance

Font styles to use
Other font styles liked:
• Poppins

Requirements
Must have
• 482 W 71st Street 14th Floor New York, NY 10157 O: +1 (212) 555 0147 F: +1 (212) 555 0182

```html
<!DOCTYPE html>
<html lang="en">
<head>
<meta charset="utf-8">
<title>Meridant Letterhead</title>
<link rel="stylesheet" href="https://fonts.googleapis.com/css2?family=Poppins:wght@400&family=Lato:wght@400&display=swap">
<style>
  :root {
    --paper: #ffffff;
    --brand-blue: #1d5ea8;
    --accent-light: #3fa9e6;
    --accent-mid: #1a86cc;
    --accent-deep: #0d5d9e;
    --ink: #1f1f1f;
  }
  html, body {
    margin: 0;
    padding: 0;
    width: 943px;
    height: 1200px;
    overflow: hidden;
    background: var(--paper);
  }
  .letterhead {
    position: relative;
    width: 943px;
    height: 1200px;
    background: var(--paper);
  }
  .brand {
    position: absolute;
    left: 106px;
    top: 74px;
    display: flex;
    align-items: center;
    gap: 12px;
  }
  .brand-dot {
    width: 22px;
    height: 22px;
    border-radius: 50%;
    background: var(--brand-blue);
  }
  .brand-name {
    font-family: "Poppins", sans-serif;
    font-weight: 400;
    font-size: 36px;
    letter-spacing: 0.5px;
    line-height: 1;
    color: var(--brand-blue);
  }
  .corner-visual {
    position: absolute;
    right: 0;
    top: 665px;
    width: 297px;
    height: 398px;
    border-radius: 150px 0 0 150px;
    background: radial-gradient(ellipse at 35% 40%, var(--accent-light) 0%, var(--accent-mid) 45%, var(--accent-deep) 100%);
    opacity: 0.9;
  }
  .contact-bar {
    position: absolute;
    top: 1100px;
    left: 0;
    width: 100%;
    font-family: "Lato", sans-serif;
    font-size: 12.5px;
    letter-spacing: 0.2px;
    color: var(--ink);
  }
  .contact-item {
    position: absolute;
    display: flex;
    align-items: center;
    gap: 5px;
    white-space: nowrap;
  }
  .contact-item svg { fill: var(--brand-blue); }
  .contact-address { left: 106px; }
  .contact-office { left: 484px; }
  .contact-fax { left: 694px; }
</style>
</head>
<body>
  <div class="letterhead">
    <header class="brand">
      <span class="brand-dot"></span>
      <span class="brand-name">MERIDANT</span>
    </header>

    <div class="corner-visual" role="img" aria-label="Glossy blue abstract connected-spheres artwork"></div>

    <footer class="contact-bar">
      <div class="contact-item contact-address">
        <svg width="9" height="12" viewBox="0 0 9 12" aria-hidden="true"><path d="M4.5 0A4.5 4.5 0 0 0 0 4.5C0 8 4.5 12 4.5 12S9 8 9 4.5A4.5 4.5 0 0 0 4.5 0Zm0 6.3a1.8 1.8 0 1 1 0-3.6 1.8 1.8 0 0 1 0 3.6Z"/></svg>
        <span>482 W 71st Street 14th Floor New York, NY 10157</span>
      </div>
      <div class="contact-item contact-office">
        <svg width="8" height="12" viewBox="0 0 8 12" aria-hidden="true"><path d="M1.5 0h5A1.5 1.5 0 0 1 8 1.5v9A1.5 1.5 0 0 1 6.5 12h-5A1.5 1.5 0 0 1 0 10.5v-9A1.5 1.5 0 0 1 1.5 0Zm.2 2v6h4.6V2Zm2.3 7.2a.9.9 0 1 0 0 1.8.9.9 0 0 0 0-1.8Z"/></svg>
        <span>O: +1 (212) 555 0147</span>
      </div>
      <div class="contact-item contact-fax">
        <svg width="8" height="12" viewBox="0 0 8 12" aria-hidden="true"><path d="M1.5 0h5A1.5 1.5 0 0 1 8 1.5v9A1.5 1.5 0 0 1 6.5 12h-5A1.5 1.5 0 0 1 0 10.5v-9A1.5 1.5 0 0 1 1.5 0Zm.2 2v6h4.6V2Zm2.3 7.2a.9.9 0 1 0 0 1.8.9.9 0 0 0 0-1.8Z"/></svg>
        <span>F: +1 (212) 555 0182</span>
      </div>
    </footer>
  </div>
</body>
</html>
```